Talvin Crestline Homes needs a business card

We need a business card for a new company in Canada, Ontario. Our company is all about luxury contraction homes for our clients. Our product and services are custom projects design. Under the business logo that will be created, we want a slogan that will be a memorable phrase for consumers to remember us to tell their friends and relatives.

Additional infomation
- Brennick Solvadeu
- President / Ceo
-415.390.7628

Find point what luxury construction products and services can be done

We like to see colors:
- #663300
- and something other colors or color that would attract the client needs and wants

The final design should communicate leads from new or old clients that will grow our empire. Most of all, we try to work among the budget that clients want

NOTE
- we also need an icon for the business (Example: Pictoloop, Friendvane, and Chattorq icons)
- We want the company name to be remembered easily for clients and our distributors who would get our orders.
- we need an icon on the business cards: Friendvane and Pictoloop.

Thanks,
Talvin Crestline Homes

```html
<!DOCTYPE html>
<html lang="en">
<head>
<meta charset="utf-8">
<title>Talvin Crestline Homes – Business Card</title>
<link href="https://fonts.googleapis.com/css2?family=Questrial&display=swap" rel="stylesheet">
<style>
  :root {
    --bg: #1b1b1b;
    --card: #0d0d0d;
    --brand-brown: #8a4a1c;
    --text-light: #d9d9d9;
    --text-muted: #a8a8a8;
  }
  * { margin: 0; padding: 0; box-sizing: border-box; }
  html, body { width: 1200px; height: 900px; overflow: hidden; }
  body {
    background: radial-gradient(ellipse at 50% 40%, #242424 0%, var(--bg) 70%);
    font-family: "Questrial", "Century Gothic", sans-serif;
    color: var(--text-light);
    position: relative;
  }
  .card {
    position: absolute;
    top: 220px;
    width: 520px;
    height: 310px;
    background: var(--card);
    border-radius: 22px;
    box-shadow: 0 18px 40px rgba(0,0,0,0.6);
  }
  .card--info { left: 50px; }
  .card--brand { left: 630px; display: flex; flex-direction: column; align-items: center; justify-content: center; }

  .brand-mark { display: flex; align-items: center; gap: 10px; }
  .brand-mark__square { width: 14px; height: 14px; background: var(--brand-brown); }
  .brand-mark__name { letter-spacing: 0.06em; text-transform: uppercase; color: var(--text-light); }

  .card--brand .brand-mark__square { width: 22px; height: 22px; }
  .card--brand .brand-mark__name { font-size: 25px; }
  .brand-tagline {
    margin-top: 12px;
    font-size: 11px;
    letter-spacing: 0.08em;
    text-transform: uppercase;
    color: var(--brand-brown);
  }

  .card--info .brand-mark { position: absolute; left: 34px; top: 32px; }
  .card--info .brand-mark__name { font-size: 14px; }

  .contact { position: absolute; left: 34px; bottom: 34px; font-size: 12px; color: var(--text-light); }
  .contact__row { display: flex; align-items: center; gap: 8px; margin-top: 6px; }
  .contact__row svg { width: 11px; height: 11px; fill: var(--brand-brown); }

  .person { position: absolute; right: 34px; top: 70px; text-align: right; }
  .person__name { font-size: 25px; color: #f2f2f2; }
  .person__title { font-size: 13px; color: var(--brand-brown); margin-top: 4px; }

  .services { list-style: none; margin-top: 14px; font-size: 12px; color: var(--text-muted); }
  .services li { display: flex; justify-content: flex-end; align-items: center; gap: 8px; line-height: 1.55; }
  .services svg { width: 11px; height: 11px; }

  .lockup {
    position: absolute;
    right: 60px;
    bottom: 60px;
    display: flex;
    flex-direction: column;
    align-items: center;
    gap: 14px;
  }
  .lockup__square { width: 60px; height: 60px; background: var(--brand-brown); }
  .lockup__name { font-size: 24px; letter-spacing: 0.05em; text-transform: uppercase; color: #e8e8e8; }
</style>
</head>
<body>
  <section class="card card--info">
    <div class="brand-mark">
      <span class="brand-mark__square"></span>
      <span class="brand-mark__name">Talvin Crestline Homes</span>
    </div>

    <div class="person">
      <p class="person__name">Brennick Solvadeu</p>
      <p class="person__title">President / Ceo</p>
      <ul class="services">
        <li>Custom Project Designs <svg viewBox="0 0 12 12"><rect x="0.5" y="2.5" width="9" height="9" fill="none" stroke="#8a4a1c"/><path d="M2 6l3 3 6-8" fill="none" stroke="#8a4a1c" stroke-width="1.4"/></svg></li>
        <li>Home Renovations <svg viewBox="0 0 12 12"><rect x="0.5" y="2.5" width="9" height="9" fill="none" stroke="#8a4a1c"/><path d="M2 6l3 3 6-8" fill="none" stroke="#8a4a1c" stroke-width="1.4"/></svg></li>
        <li>Kitchen Remodeling <svg viewBox="0 0 12 12"><rect x="0.5" y="2.5" width="9" height="9" fill="none" stroke="#8a4a1c"/><path d="M2 6l3 3 6-8" fill="none" stroke="#8a4a1c" stroke-width="1.4"/></svg></li>
        <li>Exterior Design / Interior Design <svg viewBox="0 0 12 12"><rect x="0.5" y="2.5" width="9" height="9" fill="none" stroke="#8a4a1c"/><path d="M2 6l3 3 6-8" fill="none" stroke="#8a4a1c" stroke-width="1.4"/></svg></li>
        <li>Additions <svg viewBox="0 0 12 12"><rect x="0.5" y="2.5" width="9" height="9" fill="none" stroke="#8a4a1c"/><path d="M2 6l3 3 6-8" fill="none" stroke="#8a4a1c" stroke-width="1.4"/></svg></li>
        <li>Garages <svg viewBox="0 0 12 12"><rect x="0.5" y="2.5" width="9" height="9" fill="none" stroke="#8a4a1c"/><path d="M2 6l3 3 6-8" fill="none" stroke="#8a4a1c" stroke-width="1.4"/></svg></li>
        <li>Basements &amp; Bathrooms <svg viewBox="0 0 12 12"><rect x="0.5" y="2.5" width="9" height="9" fill="none" stroke="#8a4a1c"/><path d="M2 6l3 3 6-8" fill="none" stroke="#8a4a1c" stroke-width="1.4"/></svg></li>
      </ul>
    </div>

    <div class="contact">
      <p class="contact__row">
        <svg viewBox="0 0 24 24"><path d="M6.6 10.8a15.1 15.1 0 0 0 6.6 6.6l2.2-2.2a1 1 0 0 1 1-.25 11.4 11.4 0 0 0 3.6.57 1 1 0 0 1 1 1V20a1 1 0 0 1-1 1A17 17 0 0 1 3 4a1 1 0 0 1 1-1h3.5a1 1 0 0 1 1 1c0 1.25.2 2.45.57 3.57a1 1 0 0 1-.25 1z"/></svg>
        415.390.7628
      </p>
      <p class="contact__row">
        <svg viewBox="0 0 24 24"><path d="M2 5h20v14H2z M2 5l10 8 10-8" /></svg>
        hello@talvincrestline.ca
      </p>
    </div>
  </section>

  <section class="card card--brand">
    <div class="brand-mark">
      <span class="brand-mark__square"></span>
      <span class="brand-mark__name">Talvin Crestline Homes</span>
    </div>
    <p class="brand-tagline">Home Renovations &nbsp;|&nbsp; Custom Project Design</p>
  </section>

  <div class="lockup">
    <span class="lockup__square"></span>
    <span class="lockup__name">Talvin Crestline Homes</span>
  </div>
</body>
</html>
```